I need to have a full website designed for a new consultancy business I'm trying to establish. It's called Brightpath consult. I need an English version to begin with, and then there should be a Danish version as well, but I'll translate that myself. Just be aware that I need two language versions. The consultancy field that I'm targeting is Leadership - and specialist development. I offer to facilitate corporate academies for global companies as well as specific workshops within leadership- or team development, strategy sessions, personal coaching and facilitation of D&I (Diversity and inclusion) workshops. BTW my logo is not in high resolution - I need that as well.

Target Market(s)

Larger companies that has a need for developing their inhouse leadership capabilities or that wants to develop their specialists to take on more responsibility.

Industry/Entity Type

Consultancy business

Coding

Number of Pages Required

Requirements
Must have
• Introduction site with a catch phrase. Book a meeting. Services that's beeing offered. Blog site with white papers etc. Language toggle (Danish/English). Cases/testimonials. About site. Contact site.

```html
<!DOCTYPE html>
<html lang="en">
<head>
<meta charset="utf-8">
<title>Brightpath consult – Leadership that works in practice</title>
<link rel="stylesheet" href="https://fonts.googleapis.com/css2?family=Bebas+Neue&family=Poppins:wght@400;500&display=swap">
<style>
:root{
  --navy-900:#06131f;
  --navy-800:#0a1c2d;
  --navy-700:#0e2a42;
  --navy-600:#143b5c;
  --blue:#2a84d2;
  --blue-band:#1f70b8;
  --white:#ffffff;
  --muted:#c9d4df;
  --head:'Bebas Neue',Impact,sans-serif;
  --body:'Poppins',Arial,sans-serif;
}
html,body{margin:0;padding:0;overflow:hidden;}
body{background:var(--navy-900);color:var(--white);font-family:var(--body);}
.page{position:relative;width:1200px;height:3379px;overflow:hidden;
  background:linear-gradient(180deg,#123c5e 0%,#0c2a44 12%,#0a2035 28%,#08192a 45%,#071624 60%,#081c2f 78%,#081c2f 83%);}
.abs{position:absolute;}
h1,h2,h3{font-family:var(--head);font-weight:400;margin:0;letter-spacing:.5px;}
p{margin:0;}
.accent{color:var(--blue);}
.btn{position:absolute;display:flex;align-items:center;justify-content:center;font-size:13px;text-decoration:none;letter-spacing:.3px;}
.btn-blue{background:var(--blue);color:var(--white);}
.btn-white{background:var(--white);color:var(--navy-700);}

/* nav */
.brand{font-family:var(--head);font-size:40px;color:var(--white);line-height:1;}
.nav{top:25px;right:93px;display:flex;gap:35px;align-items:center;font-size:12px;}
.nav a{color:var(--white);text-decoration:none;}
.lang{display:flex;align-items:center;gap:6px;}
.flag{width:16px;height:11px;background:#c8102e;border:1px solid #fff;box-sizing:border-box;}

/* hero */
.hero-title{left:93px;top:262px;font-size:56px;line-height:48px;}
.hero-text{left:93px;top:371px;width:470px;font-size:13px;line-height:21px;color:var(--muted);}

/* about */
.eyebrow{left:0;width:1200px;top:788px;text-align:center;font-size:12px;color:var(--blue);}
.about-title{left:0;width:1200px;top:810px;text-align:center;font-size:46px;line-height:47px;}
.card{position:absolute;left:596px;width:510px;box-sizing:border-box;padding:44px 46px;background:rgba(10,26,48,.85);}
.card h3{font-size:23px;margin-bottom:10px;}
.card p{font-size:11.5px;line-height:19px;color:var(--muted);}

/* cta strip */
.cta-strip{left:126px;top:1515px;width:800px;height:147px;background:linear-gradient(90deg,#2377c2,#2a84d2 70%,#1d6aae);}
.cta-strip h2{position:absolute;left:60px;top:36px;font-size:31px;line-height:35px;}

/* services */
.section-title{left:0;width:1200px;text-align:center;}
.svc{position:absolute;width:290px;}
.svc h3{font-size:24px;margin-bottom:6px;}
.svc p{font-size:11.5px;line-height:19px;color:var(--muted);}
.svc.right-al{text-align:right;}

/* empower */
.emp-title{left:93px;top:2418px;font-size:44px;line-height:47px;}
.emp-text{left:93px;top:2572px;width:520px;font-size:12.5px;line-height:21px;color:var(--muted);}

/* bottom band */
.band{left:0;top:2810px;width:1200px;height:508px;background:linear-gradient(160deg,#2682cf,#1c6db4 60%,#1a66a9);}
.band h2{position:absolute;left:622px;top:148px;font-size:44px;line-height:47px;}
.band p{position:absolute;left:622px;top:307px;font-size:13px;}
.footer{left:0;top:3318px;width:1200px;height:61px;background:var(--navy-900);font-size:12.5px;}
.footer .copy{position:absolute;left:93px;top:22px;}
.footer .links{position:absolute;right:93px;top:22px;display:flex;gap:28px;}
.footer a{color:var(--white);text-decoration:none;}
</style>
</head>
<body>
<div class="page">

  <!-- header -->
  <div class="abs brand" style="left:93px;top:22px;">BRIGHTPATH</div>
  <nav class="abs nav">
    <a href="#" aria-label="Home"><svg width="14" height="13" viewBox="0 0 14 13"><path d="M7 0 L14 6 H12 V13 H8.5 V9 H5.5 V13 H2 V6 H0 Z" fill="#2a84d2"/></svg></a>
    <a href="#">SERVICES</a>
    <a href="#">ABOUT</a>
    <a href="#">CONTACT</a>
    <span class="lang"><span class="flag"></span>EN <svg width="9" height="6" viewBox="0 0 9 6"><path d="M1 1 L4.5 4.5 L8 1" stroke="#fff" fill="none"/></svg></span>
  </nav>

  <!-- hero -->
  <h1 class="abs hero-title">LEADERSHIP<br>THAT WORKS IN PRACTICE</h1>
  <p class="abs hero-text">I help specialists and managers take on even more responsibility, set clear direction and create effective collaborations.</p>
  <a class="btn btn-blue" href="#" style="left:93px;top:430px;width:156px;height:42px;">BOOK A MEETING</a>

  <svg class="abs" style="left:560px;top:90px;" width="550" height="570" viewBox="560 90 550 570">
    <defs>
      <linearGradient id="portraitTone" x1="0" y1="0" x2="0" y2="1">
        <stop offset="0" stop-color="#c99a7a"/><stop offset=".45" stop-color="#8a6e66"/><stop offset="1" stop-color="#14243d"/>
      </linearGradient>
    </defs>
    <polygon points="830,240 630,480 1015,480" fill="#2a84d2"/>
    <polygon role="img" aria-label="Portrait of the consultant in a navy blazer" points="845,95 575,650 1092,645" fill="url(#portraitTone)"/>
  </svg>

  <svg class="abs" style="left:591px;top:688px;" width="18" height="27" viewBox="0 0 18 27">
    <rect x="1" y="1" width="16" height="25" rx="8" fill="none" stroke="#fff" stroke-width="1.5"/>
    <line x1="9" y1="7" x2="9" y2="12" stroke="#fff" stroke-width="1.5"/>
  </svg>

  <!-- about -->
  <p class="abs eyebrow">About Brightpath</p>
  <h2 class="abs about-title">LEADERSHIP IS NOT ABOUT TITLES -<br>IT’S ABOUT TAKING RESPONSIBILITY FOR THE <span class="accent">BUSINESS</span>,<br><span class="accent">COLLABORATION</span> AND DEVELOPMENT</h2>

  <svg class="abs" style="left:90px;top:1005px;" width="485" height="415" viewBox="90 1005 485 415">
    <polygon points="327,1010 95,1415 570,1415" fill="#2a84d2"/>
    <polygon role="img" aria-label="Photo of a smiling business team standing with arms crossed" points="327,1062 132,1392 525,1392" fill="#9aa3ab"/>
  </svg>

  <div class="card" style="top:1030px;height:183px;border:2px solid #13304f;">
    <h3>THE PURPOSE OF BRIGHTPATH</h3>
    <p>I help organizations get the full potential out of their organization – whether it’s about leaders, specialists or teams. I work with practical measures that create impact and development, not just inspiration.</p>
  </div>
  <div class="card" style="top:1223px;height:182px;">
    <h3>SPECIALISTS WITH INCREASED RESPONSIBILITY</h3>
    <p>We see companies continuing to place greater responsibility on their specialists, which is why I see it as a necessity that companies not only invest in management development, but also give their specialists a necessary skills boost so they can take on greater responsibility.</p>
  </div>

  <!-- curious strip -->
  <div class="abs cta-strip"><h2>CURIOUS ABOUT HOW<br>WE WORK WITH LEADERS AND SPECIALISTS IN PRACTICE</h2></div>
  <svg class="abs" style="left:860px;top:1485px;" width="215" height="185" viewBox="860 1485 215 185">
    <polygon points="968,1490 865,1666 1072,1666" fill="#2a84d2"/>
    <polygon points="968,1508 882,1657 1055,1657" fill="#071624"/>
    <text x="966" y="1630" text-anchor="middle" font-family="Poppins, Arial, sans-serif" font-weight="500" font-size="70" fill="#fff">?</text>
  </svg>

  <!-- services -->
  <h2 class="abs section-title" style="top:1763px;font-size:44px;">OUR SERVICES</h2>
  <p class="abs section-title" style="top:1820px;font-size:12.5px;">Tailored solutions that create lasting impact.</p>

  <svg class="abs" style="left:380px;top:1880px;" width="460" height="365" viewBox="380 1880 460 365">
    <polygon points="596,1884 385,2238 812,2241" fill="#2a84d2"/>
    <polygon points="596,1926 418,2222 778,2222" fill="#06131f"/>
    <g fill="#081c2f" stroke="#2a84d2" stroke-width="1.2">
      <polygon points="556,1900 518,1964 594,1964"/>
      <polygon points="640,1900 602,1964 678,1964"/>
      <polygon points="486,2018 448,2082 524,2082"/>
      <polygon points="711,2018 673,2082 749,2082"/>
      <polygon points="421,2138 383,2202 459,2202"/>
      <polygon points="798,2138 760,2202 836,2202"/>
    </g>
    <g fill="none" stroke="#fff" stroke-width="1.3">
      <rect x="549" y="1938" width="14" height="10"/>
      <circle cx="640" cy="1944" r="6"/>
      <circle cx="486" cy="2062" r="6"/>
      <path d="M704 2060 l5 5 l9 -9"/>
      <rect x="414" y="2176" width="14" height="12"/>
      <rect x="791" y="2176" width="14" height="12"/>
    </g>
  </svg>
  <div class="abs brand" style="left:418px;top:2110px;width:356px;text-align:center;font-size:50px;">BRIGHTPATH</div>

  <div class="svc right-al" style="left:187px;top:1878px;"><h3>CORPORATE ACADEMIES</h3><p>Design and facilitation of structured academies for leadership and specialist development across global organisations.</p></div>
  <div class="svc" style="left:742px;top:1878px;"><h3>PERSONAL COACHING</h3><p>One-to-one coaching focused on strengthening leadership presence, decision-making and growth.</p></div>
  <div class="svc right-al" style="left:98px;top:2003px;"><h3>LEADERSHIP &amp; TEAM WORKSHOPS</h3><p>Practical workshops that strengthen leadership capability and build effective team collaboration.</p></div>
  <div class="svc" style="left:783px;top:2003px;width:320px;"><h3>DIVERSITY &amp; INCLUSION WORKSHOPS</h3><p>Inclusive facilitation and practical interventions that increase engagement and innovation.</p></div>
  <div class="svc right-al" style="left:53px;top:2130px;"><h3>STRATEGY SESSIONS</h3><p>Facilitated strategy sessions to set clear direction and align teams around measurable goals.</p></div>
  <div class="svc" style="left:846px;top:2130px;width:240px;"><h3>BESPOKE PROGRAMMES</h3><p>Custom programmes combining workshops, coaching and follow-up to sustain change.</p></div>

  <!-- empowering -->
  <h2 class="abs emp-title">EMPOWERING<br>SPECIALISTS WITH <span class="accent">GREATER</span><br>RESPONSIBILITY</h2>
  <p class="abs emp-text">We see companies placing more responsibility on specialists. Brightpath helps organisations invest in both leadership development and specialist competency so teams can perform stronger and deliver impact.</p>

  <svg class="abs" style="left:670px;top:2355px;" width="430" height="355" viewBox="670 2355 430 355">
    <polygon points="885,2362 690,2705 1093,2705" fill="#2a84d2"/>
    <polygon role="img" aria-label="Photo of a smiling young professional pointing forward" points="885,2412 717,2685 1055,2685" fill="#6d6a6a"/>
    <polygon points="758,2375 676,2530 836,2525" fill="#2a84d2"/>
    <polygon role="img" aria-label="Photo of colleagues discussing around a desk" points="758,2398 692,2520 823,2516" fill="#b9c2c9"/>
  </svg>

  <!-- bottom band -->
  <div class="abs band">
    <div class="brand" style="position:absolute;left:97px;top:205px;font-size:64px;">BRIGHTPATH</div>
    <h2>CURIOUS ABOUT HOW<br>WE WORK WITH LEADERS<br>AND SPECIALISTS IN PRACTICE?</h2>
    <p>Book a meeting to discuss a tailored programme for your organisation.</p>
    <a class="btn btn-white" href="#" style="left:622px;top:332px;width:156px;height:42px;">BOOK A MEETING</a>
  </div>

  <footer class="abs footer">
    <span class="copy">© "Brightpath consult" 2025</span>
    <span class="links"><a href="#">Privacy</a><a href="#">Terms</a><a href="#">Netlink</a></span>
  </footer>
</div>
</body>
</html>
```